Business card design needed

Looking for an innovative design that portrays a professional image for our company. We are a structural steel erection, EWP and crane hire company. We are looking at having business and contact details on front of card and perhaps a list of what we hire on the back of the card. Our company machine colours are royal blue and silver at present but would be open to change with our cards...
Updates
We are looking for double sided designs due to the amount of information required on the card
The Logo uploaded if the logo we have been using, however our company name has changed to just "Steady Summit Lifting". I have uploaded the image just for ideas...
Reason: Allowing more time for more design submissions
Reason: Want more dedigns
Target Market(s)
Construction/Industrial
Industry/Entity Type
Structural Steel
Contact Information for Business Card
Business Name: Steady Summit Lifting
Specialising in Structural Steel Erection, Equipment & Crane Hire
Address: 27 Corwin Street, Balmoral Q 4571
Site Contact: Dale Morven - 0431 597 203 - dale@sslifting.example
Office Contact: Lina Fairbrook - 0419 735 214 - lina@sslifting.example
We hire Forklifts, Telehandlers, Scissor-lifts, Boom-lifts, 3T Mini Cranes, 16T/20T Bexlo, Prime mover with extendable trailer (13.5-22m), Qualified Boilermakers,Riggers and Dogman.
Logo Text
Steady Summit Lifting or SSL
Logo styles of interest
Emblem Logo
Look and feel

```html
<!DOCTYPE html>
<html lang="en">
<head>
<meta charset="utf-8">
<title>Steady Summit Lifting – Business Card</title>
<link href="https://fonts.googleapis.com/css2?family=Questrial&family=Saira:wght@700&display=swap" rel="stylesheet">
<style>
  :root {
    --page-bg: #f0f0f0;
    --card-bg: #ffffff;
    --royal: #1c3b94;
    --cyan: #00b2cc;
    --card-edge: #d6d6d6;
  }
  html, body {
    margin: 0;
    width: 1200px;
    height: 900px;
    overflow: hidden;
    background: var(--page-bg);
    font-family: "Questrial", "Futura", sans-serif;
  }
  .card {
    position: absolute;
    width: 483px;
    height: 290px;
    background: var(--card-bg);
    border-right: 1px solid var(--card-edge);
    border-bottom: 1px solid var(--card-edge);
    overflow: hidden;
  }
  .card-back { left: 463px; top: 119px; }
  .card-front { left: 162px; top: 481px; }
  .accent-area {
    position: absolute;
    inset: 0;
    width: 100%;
    height: 100%;
  }
  .hire-list {
    position: absolute;
    left: 63px;
    top: 58px;
    margin: 0;
    color: var(--cyan);
    font-size: 14.6px;
    line-height: 19.2px;
  }
  .contact {
    position: absolute;
    top: 181px;
    margin: 0;
    color: var(--royal);
    font-size: 11.2px;
    line-height: 16.8px;
  }
  .contact-office { left: 63px; }
  .contact-site { right: 66px; text-align: right; top: 179px; }
  .front-content {
    position: absolute;
    left: 0;
    right: 0;
    top: 110px;
    text-align: center;
  }
  .company-name {
    margin: 0;
    color: var(--royal);
    font-family: "Saira", "Eurostile", sans-serif;
    font-weight: 700;
    font-size: 29px;
    letter-spacing: 1px;
    line-height: 32px;
  }
  .specialty {
    margin: 16px 0 0;
    color: var(--cyan);
    font-size: 11.2px;
    line-height: 15px;
  }
  .address {
    margin: 11px 0 0;
    color: var(--royal);
    font-size: 11.2px;
    line-height: 15px;
  }
</style>
</head>
<body>

<section class="card card-back">
  <svg class="accent-area" viewBox="0 0 540 325" preserveAspectRatio="none" role="img" aria-label="Decorative corner band in royal blue, cyan and silver tones">
    <defs>
      <linearGradient id="accentBack" x1="0" y1="0" x2="1" y2="0.5">
        <stop offset="0" stop-color="#9aa6c4"/>
        <stop offset="0.5" stop-color="#1c3b94"/>
        <stop offset="1" stop-color="#00b2cc"/>
      </linearGradient>
    </defs>
    <path d="M30,0 Q340,18 540,165 L540,0 Z" fill="url(#accentBack)"/>
  </svg>

  <p class="hire-list">WE HIRE:<br>
    Forklifts, Telehandlers, Scissor-lifts,<br>
    Boom-lifts, 3T Mini Cranes, 16T/20T Bexlo,<br>
    Prime mover with extendable trailer (13.5-22m),<br>
    Qualified Boilermakers,Riggers and Dogman.</p>

  <p class="contact contact-office">OFFICE CONTACT :<br>
    Lina Fairbrook - 0419 735 214<br>
    lina@sslifting.example</p>

  <p class="contact contact-site">SITE CONTACT:<br>
    Dale Morven - 0431 597 203<br>
    dale@sslifting.example</p>
</section>

<section class="card card-front">
  <svg class="accent-area" viewBox="0 0 540 325" preserveAspectRatio="none" role="img" aria-label="Decorative corner band in royal blue, cyan and silver tones">
    <defs>
      <linearGradient id="accentFront" x1="0" y1="0" x2="1" y2="0.5">
        <stop offset="0" stop-color="#1c3b94"/>
        <stop offset="0.5" stop-color="#00b2cc"/>
        <stop offset="1" stop-color="#9aa6c4"/>
      </linearGradient>
    </defs>
    <path d="M520,0 Q210,15 0,170 L0,0 Z" fill="url(#accentFront)"/>
  </svg>

  <div class="front-content">
    <h1 class="company-name">Steady Summit Lifting</h1>
    <p class="specialty">SPECIALISING IN<br>Structural Steel Erection,<br>Equipment &amp; Crane</p>
    <p class="address">HIRE ADDRESS<br>27 Corwin Street, Balmoral Q 4571</p>
  </div>
</section>

</body>
</html>
```